Comp & Pen Prep Tip Sheet for Veterans

I need a flyer/brochure/card with tips to help prepare veterans for their upcoming Comp & Pen Exams. Needs to be colorful and have vectors/images that correspond with teach tip. I have attached a word document with the language to include. This will go out with our welcome kit for veterans to reference before their exam.

Target Market(s)

Veterans

Industry/Entity Type

Legal/Non-Profit Organization/Medical

Colors
0054AA
0677BA
7BADD7
CADEEF
E8F1F8

Requirements
Must have
• Vectors/easy to follow

```html
<!DOCTYPE html>
<html lang="en">
<head>
<meta charset="UTF-8">
<title>Comp &amp; Pen Exam Tip Sheet</title>
<link rel="stylesheet" href="https://fonts.googleapis.com/css2?family=Oswald:wght@500;600;700&family=Source+Sans+3:wght@400;600;700&display=swap">
<style>
:root{
  --stage:#0e1a2a;
  --navy:#1a3f8a;
  --blue:#0054AA;
  --blue-mid:#0677BA;
  --blue-light:#7BADD7;
  --red:#e3202a;
  --ink:#1c3a7a;
  --text:#333b48;
  --white:#ffffff;
}
*{box-sizing:border-box;margin:0;padding:0}
html,body{width:1200px;height:1200px;overflow:hidden}
body{background:var(--stage);font-family:"Source Sans 3",sans-serif;position:relative}
.flyer{position:absolute;left:171px;top:49px;width:857px;height:1101px;background:var(--white);overflow:hidden}
.hero{position:absolute;left:0;top:0;width:857px;height:513px;
  background:radial-gradient(ellipse at 50% 60%,#5a97da 0%,#2465b6 45%,#0f4291 100%)}
.hero-photo{position:absolute;left:0;top:0;width:857px;height:290px}
.brand{position:absolute;left:24px;top:70px;width:160px;text-align:center;color:var(--white)}
.brand-name{display:flex;align-items:center;justify-content:center;gap:7px;font-family:"Oswald",sans-serif;font-weight:600;font-size:17px;line-height:1.15;text-transform:uppercase}
.brand-dot{width:12px;height:12px;border-radius:50%;background:var(--white);flex:none}
.brand-since{margin-top:30px;font-family:"Oswald",sans-serif;font-weight:500;font-size:8px;color:#1d2630}
.title{position:absolute;top:296px;left:0;width:857px;text-align:center;font-family:"Oswald",sans-serif;font-weight:700;font-size:53px;line-height:66px;color:var(--white);text-shadow:3px 3px 0 #173f86}
.intro{position:absolute;top:366px;left:40px;width:777px;text-align:center;color:var(--white);font-size:12.6px;line-height:17.6px}
.intro p{margin-bottom:8.5px}
.notice{position:absolute;top:481px;left:0;width:857px;height:21px}
.notice svg{position:absolute;left:0;top:0}
.notice span{position:absolute;left:0;width:857px;top:2px;text-align:center;color:var(--white);font-weight:700;font-size:12px;line-height:17px}
.tips-head{position:absolute;top:513px;left:0;width:857px;height:50px;background:var(--navy);color:var(--white);text-align:center;font-family:"Oswald",sans-serif;font-weight:700;font-size:38px;line-height:50px}
.tips{position:absolute;top:563px;left:0;width:857px;height:518px;display:grid;grid-template-columns:285px 286px 284px;grid-template-rows:259px 258px;gap:1px;background:#e2e4e8}
.tip{background:linear-gradient(#f8f9fa,#eef0f2);padding:8px 24px 0;text-align:center}
.tip-row2{padding-top:12px}
.tip-icon{height:40px;display:flex;justify-content:center;align-items:center}
.tip-title{margin:5px 0 14px;font-family:"Oswald",sans-serif;font-weight:600;font-size:19.5px;line-height:26px;color:var(--ink)}
.tip-body{color:var(--text);font-size:12.6px;line-height:16.3px;text-align:justify;text-align-last:center}
.tip-body p+p{margin-top:16.3px}
.foot{position:absolute;left:0;bottom:0;width:857px;height:20px}
</style>
</head>
<body>
<div class="flyer">
  <section class="hero">
    <svg class="hero-photo" viewBox="0 0 857 290" width="857" height="290" role="img" aria-label="Photo of a soldier's camouflage uniform sleeve with an American flag patch">
      <defs>
        <linearGradient id="camo" x1="0" y1="0" x2="1" y2="0.3">
          <stop offset="0" stop-color="#8d9588"/>
          <stop offset="0.35" stop-color="#a89f86"/>
          <stop offset="0.6" stop-color="#7c7a5d"/>
          <stop offset="1" stop-color="#9b8a72"/>
        </linearGradient>
      </defs>
      <path d="M0 0H857V188Q428 370 0 188Z" fill="url(#camo)"/>
      <path d="M0 188Q428 370 857 188" fill="none" stroke="#1757ae" stroke-width="6"/>
    </svg>
    <div class="brand">
      <div class="brand-name"><span class="brand-dot"></span><span>Harbor Veterans<br>Alliance</span></div>
      <div class="brand-since">Serving Veterans Since 1993</div>
    </div>
    <h1 class="title">THE COMP &amp; PEN EXAM</h1>
    <div class="intro">
      <p>The Comp &amp; Pen Exam is your opportunity to present all the reasons you believe your condition is related to service to the physician.</p>
      <p>If your condition is not already service-connected, be sure to talk to the examiner about what happened in service that could have led to your current condition. The examiner will review your file, including your statements, service records, and treatment records, and provide a medical opinion as to whether your condition was caused or aggravated by your military service.</p>
      <p>The examiner will be observing your movements and behavior and may perform a limited physical exam to evaluate your condition.</p>
    </div>
    <div class="notice">
      <svg width="857" height="21" viewBox="0 0 857 21"><path d="M88 0H773L762 21H99Z" fill="var(--red)"/></svg>
      <span>After your Comp &amp; Pen Exam, make sure you complete the Comp &amp; Pen Exit Survey based on your experience</span>
    </div>
  </section>

  <h2 class="tips-head">THINGS TO REMEMBER FOR YOUR EXAM</h2>

  <div class="tips">
    <article class="tip">
      <div class="tip-icon"><svg width="40" height="38" viewBox="0 0 44 42" fill="var(--red)"><circle cx="15" cy="15" r="8"/><path d="M1 42Q1 26 15 26Q29 26 29 42Z"/><rect x="24" y="1" width="19" height="13" rx="6"/><path d="M27 13L25 19L32 14Z"/><circle cx="29" cy="7.5" r="1.4" fill="#fff"/><circle cx="33.5" cy="7.5" r="1.4" fill="#fff"/><circle cx="38" cy="7.5" r="1.4" fill="#fff"/></svg></div>
      <h3 class="tip-title">1.&nbsp; Talk About Your Service</h3>
      <div class="tip-body"><p>Talk about what happened in service that you believe caused or aggravated your condition. Try to be as specific as possible. If you are not comfortable discussing the details of an in-service event, you may point to statements you submitted to the VA previously for the examiner to reference. If you can, provide the examiner with a copy of these statements on the day of the exam.</p></div>
    </article>
    <article class="tip">
      <div class="tip-icon"><svg width="38" height="38" viewBox="0 0 42 42" fill="none" stroke="var(--red)" stroke-width="3"><path d="M8 10A18 18 0 0 0 10 36M34 10A18 18 0 0 1 32 36"/><circle cx="21" cy="7" r="4" fill="var(--red)" stroke="none"/><path d="M21 13V30M13 18H29M21 30L16 40M21 30L26 40" stroke-linecap="round"/></svg></div>
      <h3 class="tip-title">2.&nbsp; Trace Your Symptoms</h3>
      <div class="tip-body"><p>Discuss what symptoms you experienced immediately following your injury in service and how these symptoms have worsened over time.</p><p>Your statement will help trace the start of your symptoms back to what happened during service.</p></div>
    </article>
    <article class="tip">
      <div class="tip-icon"><svg width="40" height="36" viewBox="0 0 44 40"><path d="M22 39L4 21A11 11 0 0 1 22 6A11 11 0 0 1 40 21Z" fill="var(--red)"/><path d="M12 26L22 16L30 22" fill="none" stroke="#fff" stroke-width="3" stroke-linecap="round"/></svg></div>
      <h3 class="tip-title">3.&nbsp; Be Honest</h3>
      <div class="tip-body"><p>Be honest when describing the frequency and severity of your symptoms and how they impact your day-to-day life to the examiner; do not downplay the severity of your symptoms.</p><p>Keep in mind that the examiner will be closely monitoring your movements and behavior, including your body language and the tone of your voice.</p></div>
    </article>
    <article class="tip tip-row2">
      <div class="tip-icon"><svg width="36" height="40" viewBox="0 0 40 44" fill="none" stroke="var(--red)" stroke-width="2.5" stroke-linecap="round"><circle cx="20" cy="31" r="11"/><circle cx="20" cy="31" r="4.5" fill="var(--red)" stroke="none"/><path d="M20 2L18 9L21 10L19 16M6 6L10 12M34 6L30 12M2 14L8 16M38 14L32 16"/></svg></div>
      <h3 class="tip-title">4.&nbsp; Pain</h3>
      <div class="tip-body"><p>While the exam is not meant to be painful, you may experience slight discomfort depending on the required testing.</p><p>When testing your range of motion, be sure to tell the examiner AS SOON AS you begin to experience pain, as this contributes to your overall functional loss and should be considered in your rating.</p></div>
    </article>
    <article class="tip tip-row2">
      <div class="tip-icon"><svg width="40" height="40" viewBox="0 0 44 44"><circle cx="11" cy="25" r="6" fill="var(--red)"/><path d="M1 44Q1 33 11 33Q21 33 21 44Z" fill="var(--red)"/><rect x="18" y="2" width="24" height="18" rx="2" fill="none" stroke="var(--red)" stroke-width="2.5"/><path d="M22 20L20 27L28 20" fill="var(--red)"/><path d="M22 8H29M22 12H29M22 16H28" stroke="var(--red)" stroke-width="2"/><text x="36" y="16" font-family="Oswald,sans-serif" font-weight="700" font-size="13" fill="var(--red)" text-anchor="middle">?</text></svg></div>
      <h3 class="tip-title">5.&nbsp; Ask for Clarification</h3>
      <div class="tip-body"><p>Do not answer a question you do not understand. Ask for clarification if necessary. Do not talk to fill the space or time. Keep your conversation with the examiner limited to what happened in service, the frequency and severity of symptoms related to your condition, and how they impact your day-to-day life.</p></div>
    </article>
    <article class="tip tip-row2">
      <div class="tip-icon"><svg width="42" height="38" viewBox="0 0 46 42"><rect x="8" y="1" width="16" height="6" rx="1" fill="var(--red)"/><rect x="5" y="9" width="22" height="32" rx="3" fill="var(--red)"/><path d="M16 17V33M8 25H24" stroke="#fff" stroke-width="3"/><rect x="29" y="28" width="16" height="7" rx="3.5" fill="var(--red)"/><rect x="29" y="36" width="16" height="6" rx="3" fill="var(--red)"/></svg></div>
      <h3 class="tip-title">6.&nbsp; Medications</h3>
      <div class="tip-body"><p>If you are prescribed any medication(s) for your condition, be sure to tell the examiner the name and dosage of each medication and how often you take each. This is extremely important, because medication may mask some of your symptoms, or the use of medication(s) may be used to evaluate the severity of your condition and how much it impacts your ability to work.</p></div>
    </article>
  </div>

  <svg class="foot" width="857" height="20" viewBox="0 0 857 20">
    <path d="M0 0H560L548 20H0Z" fill="var(--navy)"/>
    <path d="M572 0H857V20H560Z" fill="var(--red)"/>
  </svg>
</div>
</body>
</html>
```